Refrigerator Banner

We are purchasing a container of refrigerators. One of our competitors overseas has a really nice sticker/canopy header on top of the light box. please see attched Pic A & Pic B.
Now, we would like to have a sort of similar look and just different enough not to upset anyone. However, this competitor is on the other side of the world, so we don't really compete with each other. So maybe the same blue but have the water thinghy a bit different.
Also, our brand name is "KORVALE Refrigeration"
I would design in the following dimensions:
• 572mm × 223mm
• 1125mm × 223mm
• 1705mm × 223mm
thanks

```html
<!DOCTYPE html>
<html lang="en">
<head>
<meta charset="utf-8">
<title>KORVALE Refrigeration – Header Banners</title>
<link rel="stylesheet" href="https://fonts.googleapis.com/css2?family=Outfit:wght@300;500&display=swap">
<style>
  :root {
    --night: #000000;
    --navy: #0a2a5e;
    --deep-blue: #0a2596;
    --royal-blue: #1239b8;
    --mid-blue: #1a5fd0;
    --bright-blue: #19a6f0;
    --cyan: #3fd0ff;
    --ice: #d8ecfb;
    --label-grey: #8a8f96;
    --white: #ffffff;
  }
  * { margin: 0; padding: 0; box-sizing: border-box; }
  html, body { width: 1200px; height: 1200px; overflow: hidden; }
  body {
    position: relative;
    background: radial-gradient(ellipse 90% 50% at 50% 100%, var(--navy) 0%, #04132e 55%, var(--night) 100%);
    background-color: var(--night);
    font-family: "Outfit", sans-serif;
    color: var(--white);
  }
  .scale-note {
    position: absolute;
    left: 77px;
    top: 182px;
    font-size: 27px;
    font-weight: 300;
    color: var(--label-grey);
  }
  .banner { position: absolute; overflow: hidden; }
  .banner--small  { left: 439px; top: 67px;  width: 696px;  height: 136px; }
  .banner--medium { left: 76px;  top: 246px; width: 1059px; height: 137px; }
  .banner--large  { left: 77px;  top: 429px; width: 1058px; height: 413px; }

  .water-photo { position: absolute; inset: 0; }

  .banner--small .water-photo {
    background:
      radial-gradient(ellipse 22% 45% at 55% 5%, rgba(63,208,255,0.85) 0%, rgba(63,208,255,0) 100%),
      radial-gradient(ellipse 30% 60% at 12% 85%, rgba(216,236,251,0.45) 0%, rgba(216,236,251,0) 100%),
      radial-gradient(ellipse 25% 55% at 30% 30%, rgba(25,166,240,0.75) 0%, rgba(25,166,240,0) 100%),
      radial-gradient(ellipse 18% 50% at 78% 55%, rgba(10,37,150,0.8) 0%, rgba(10,37,150,0) 100%),
      radial-gradient(ellipse 20% 60% at 68% 95%, rgba(63,208,255,0.35) 0%, rgba(63,208,255,0) 100%),
      linear-gradient(160deg, var(--mid-blue) 0%, var(--royal-blue) 55%, var(--deep-blue) 100%);
  }
  .banner--medium .water-photo {
    background:
      radial-gradient(ellipse 12% 70% at 8% 60%, rgba(216,236,251,0.35) 0%, rgba(216,236,251,0) 100%),
      radial-gradient(ellipse 18% 45% at 50% 10%, rgba(63,208,255,0.8) 0%, rgba(63,208,255,0) 100%),
      radial-gradient(ellipse 16% 50% at 28% 45%, rgba(25,166,240,0.7) 0%, rgba(25,166,240,0) 100%),
      radial-gradient(ellipse 14% 45% at 73% 15%, rgba(63,208,255,0.55) 0%, rgba(63,208,255,0) 100%),
      radial-gradient(ellipse 16% 55% at 82% 60%, rgba(10,37,150,0.85) 0%, rgba(10,37,150,0) 100%),
      radial-gradient(ellipse 14% 50% at 60% 90%, rgba(25,166,240,0.45) 0%, rgba(25,166,240,0) 100%),
      linear-gradient(170deg, var(--mid-blue) 0%, var(--royal-blue) 55%, var(--deep-blue) 100%);
  }
  .banner--large .water-photo {
    background:
      radial-gradient(ellipse 28% 26% at 45% 58%, rgba(216,236,251,0.9) 0%, rgba(216,236,251,0) 100%),
      radial-gradient(ellipse 20% 18% at 30% 70%, rgba(216,236,251,0.6) 0%, rgba(216,236,251,0) 100%),
      radial-gradient(ellipse 22% 14% at 30% 98%, rgba(216,236,251,0.55) 0%, rgba(216,236,251,0) 100%),
      radial-gradient(ellipse 26% 20% at 55% 12%, rgba(63,208,255,0.75) 0%, rgba(63,208,255,0) 100%),
      radial-gradient(ellipse 14% 14% at 88% 4%, rgba(63,208,255,0.7) 0%, rgba(63,208,255,0) 100%),
      radial-gradient(ellipse 22% 28% at 12% 30%, rgba(25,166,240,0.6) 0%, rgba(25,166,240,0) 100%),
      radial-gradient(ellipse 30% 30% at 38% 38%, rgba(25,166,240,0.55) 0%, rgba(25,166,240,0) 100%),
      radial-gradient(ellipse 35% 40% at 85% 45%, rgba(10,37,150,0.7) 0%, rgba(10,37,150,0) 100%),
      linear-gradient(175deg, var(--mid-blue) 0%, var(--royal-blue) 50%, var(--mid-blue) 100%);
  }

  .wordmark {
    position: absolute;
    text-align: center;
    color: var(--white);
    font-weight: 500;
    line-height: 1;
  }
  .wordmark__name { display: block; letter-spacing: -0.01em; }
  .wordmark__line { display: block; }

  .banner--small .wordmark  { right: 34px; top: 79px; }
  .banner--medium .wordmark { right: 34px; top: 76px; }
  .banner--small .wordmark__name,
  .banner--medium .wordmark__name { font-size: 31px; }
  .banner--small .wordmark__line,
  .banner--medium .wordmark__line { font-size: 13px; letter-spacing: 0.06em; margin-top: 0; }

  .banner--large .wordmark { right: 57px; top: 268px; }
  .banner--large .wordmark__name { font-size: 62px; }
  .banner--large .wordmark__line { font-size: 27px; letter-spacing: 0.08em; margin-top: 2px; }

  .signoff { left: 0; width: 1252px; top: 1016px; }
  .signoff .wordmark__name { font-size: 41px; }
  .signoff .wordmark__line { font-size: 19px; letter-spacing: 0.05em; margin-top: 1px; }
</style>
</head>
<body>
  <p class="scale-note">Not to scale</p>

  <section class="banner banner--small" aria-label="Header banner 572 × 223 mm">
    <div class="water-photo" role="img" aria-label="Close-up photograph of a splash of clear blue water"></div>
    <div class="wordmark">
      <span class="wordmark__name">KORVALE</span>
      <span class="wordmark__line">REFRIGERATION</span>
    </div>
  </section>

  <section class="banner banner--medium" aria-label="Header banner 1125 × 223 mm">
    <div class="water-photo" role="img" aria-label="Close-up photograph of a wave of splashing blue water"></div>
    <div class="wordmark">
      <span class="wordmark__name">KORVALE</span>
      <span class="wordmark__line">REFRIGERATION</span>
    </div>
  </section>

  <section class="banner banner--large" aria-label="Header banner 1705 × 223 mm">
    <div class="water-photo" role="img" aria-label="Close-up photograph of blue water splashing over bright ice"></div>
    <div class="wordmark">
      <span class="wordmark__name">KORVALE</span>
      <span class="wordmark__line">REFRIGERATION</span>
    </div>
  </section>

  <div class="wordmark signoff">
    <span class="wordmark__name">KORVALE</span>
    <span class="wordmark__line">REFRIGERATION</span>
  </div>
</body>
</html>
```